New Basketball Sports Agency need webpage design

We are a GRVO/PKL Sports agency looking for a new Webpage design. We currently have a site @ www.tqrhoopsgroup.example, and looking for someone to redesign the site.. We are also looking to redo the LOGO as well. TQR will begin its Vantage clinics also, and would like a page to promote and sign up for camp. I already have quidlane, but not sure how to add to site. Site must include:

Page for Agency updates, Client profiles, page for admin, camp registration page, flash photos, and able to filter news updates from contihoops, and KWVR sites.
Updates

Target Market(s)

European basketball clubs, USA Teams, Basketball Players, Sports Agents, Sports Directors General Managers,

Industry/Entity Type

News

```html
<!DOCTYPE html>
<html lang="en">
<head>
<meta charset="utf-8">
<title>TQR Hoops Group</title>
<link rel="stylesheet" href="https://fonts.googleapis.com/css2?family=Montserrat:wght@400;500;600;700;800&display=swap">
<style>
:root{
  --backdrop-top:#2e2a1e;
  --backdrop-bottom:#050505;
  --page:#ffffff;
  --ink:#333333;
  --muted:#777777;
  --red:#d8202a;
  --black:#050505;
  --nav-top:#3a3a3a;
  --nav-bottom:#101010;
  --gold:#f7b500;
  --gold-light:#ffd84a;
  --cream:#f3e6b8;
  --rule:#d6d6d6;
  --badge:#b9b9b9;
  --social:#e9e9e9;
  --social-ink:#222222;
  --footer-social:#5a5a5a;
}
*{box-sizing:border-box;margin:0;padding:0}
html,body{width:1108px;height:1200px;overflow:hidden}
body{
  position:relative;
  font-family:"Montserrat",sans-serif;
  color:var(--ink);
  background:
    radial-gradient(ellipse 260px 160px at 90px 500px,rgba(150,130,40,.35),transparent),
    radial-gradient(ellipse 220px 140px at 1030px 620px,rgba(150,130,40,.3),transparent),
    linear-gradient(180deg,var(--backdrop-top) 0%,#2a2a28 35%,#1a1a18 60%,var(--backdrop-bottom) 85%);
}
.abs{position:absolute}
.page{left:185px;top:74px;width:739px;height:1126px;background:var(--page)}

/* brand */
.brand{left:186px;top:30px;display:flex;align-items:center;gap:8px}
.brand-dot{width:62px;height:62px;border-radius:50%;background:#f28a12}
.brand-name{font-weight:800;font-size:34px;color:var(--ink);background:var(--page);padding:2px 8px;border-radius:4px}

.social{top:22px;display:flex;gap:6px;left:763px}
.social span{width:36px;height:36px;border-radius:50%;background:var(--social);color:var(--social-ink);
  font-size:11px;font-weight:700;display:flex;align-items:center;justify-content:center}

/* navigation */
.nav{left:309px;top:90px;width:619px;height:30px;
  background:linear-gradient(180deg,var(--nav-top),var(--nav-bottom));display:flex;align-items:center}
.nav a{color:#fff;text-decoration:none;font-size:13px;letter-spacing:-.2px;position:absolute;transform:translateX(-50%)}
.nav .sep{position:absolute;top:8px;height:14px;border-left:1px dotted #888}

/* hero */
.hero{left:196px;top:133px;width:717px;height:336px;background:#0c0c0c;overflow:hidden}
.hero-player{left:0;top:0;width:240px;height:336px;
  background:linear-gradient(180deg,#2a1416 0%,#6e1c24 40%,#5a141a 75%,#1a0c0c 100%)}
.hero-net{right:0;top:0;width:300px;height:336px;
  background:radial-gradient(circle 120px at 210px 200px,#e8391e,#b3200f 60%,transparent 62%),
  linear-gradient(200deg,#6a6a6a,#2a2a2a 40%,#0c0c0c 70%)}
.hero-title{left:224px;top:26px;font-weight:800;font-size:72px;line-height:1;
  background:linear-gradient(180deg,var(--gold-light),var(--gold));-webkit-background-clip:text;color:transparent}
.hero-sub{left:224px;top:100px;font-weight:800;font-size:42px;line-height:42px;color:var(--cream)}
.hero-from{left:224px;top:210px;font-weight:700;font-size:19px;color:#fff}
.hero-date{left:223px;top:228px;font-weight:800;font-size:48px;color:#fff;line-height:1.1}
.hero-year{left:227px;top:278px;font-weight:800;font-size:35px;color:#fff}
.signup{left:361px;top:283px;width:178px;height:35px;background:var(--red);border:1px solid #ff5a5a;
  color:#fff;font-weight:800;font-size:19px;display:flex;align-items:center;justify-content:center}
.dots{left:628px;top:315px;display:flex;gap:8px}
.dots i{width:11px;height:11px;border-radius:50%;background:var(--gold)}
.dots i:first-child{background:#fff}

/* section heads */
.section-head{height:40px;color:#fff;font-weight:800;font-size:27px;padding-left:10px;line-height:42px}
.section-head.red{background:var(--red)}
.section-head.dark{background:var(--black)}

.news-feature{left:196px;top:532px;width:353px;height:195px;
  background:linear-gradient(180deg,#5a2a22 0%,#8a6a50 40%,#c7a96a 60%,#3a2a28 100%)}
.news-caption{left:196px;top:682px;width:353px;height:45px;background:rgba(20,20,20,.82);
  color:#fff;font-weight:700;font-size:14px;line-height:17px;padding:6px 12px}
.news-item{left:196px;width:353px;height:61px}
.thumb{position:absolute;left:0;top:0;width:90px;height:61px;background:linear-gradient(160deg,#7a2a26,#b08a66 50%,#3a3440)}
.news-item h3,.video-item h3{font-weight:400;color:var(--ink)}
.news-item h3{position:absolute;left:102px;top:0;font-size:14.5px;line-height:16px}
.meta{font-size:11.5px;color:var(--muted)}
.news-item .meta{position:absolute;left:102px;top:36px}

.video-item{left:560px;width:353px;height:87px}
.video-thumb{position:absolute;left:0;top:0;width:124px;height:87px;background:linear-gradient(150deg,#4a4a52,#1e2a3a 60%,#0a0a0a);border:3px solid #111}
.video-item h3{position:absolute;left:138px;top:2px;font-size:15px;line-height:17px;width:210px}
.video-item .meta{position:absolute;left:138px;top:66px}
.video-rule{left:560px;width:353px;border-top:1px solid var(--rule)}

.badges{left:196px;top:1012px;width:717px;height:52px}
.badge{position:absolute;top:6px;height:42px;background:var(--badge);border-radius:4px}

.footer{left:196px;top:1075px;width:717px;height:111px;background:var(--black);color:#fff}
.footer-mark{position:absolute;left:14px;top:17px;display:flex;align-items:center;gap:5px}
.footer-mark i{width:42px;height:42px;border-radius:50%;background:#777}
.footer-mark b{font-size:18px;font-weight:800;color:#cfcfcf}
.footer h4{position:absolute;left:114px;top:24px;font-weight:400;font-size:21px}
.footer-links{position:absolute;left:114px;top:54px;font-size:10px;display:flex;gap:10px}
.footer-social{position:absolute;left:540px;top:28px;display:flex;gap:4px}
.footer-social span{width:37px;height:37px;border-radius:50%;background:var(--footer-social);
  font-size:11px;font-weight:700;color:#111;display:flex;align-items:center;justify-content:center}
.footer-rule{position:absolute;left:0;top:81px;width:717px;border-top:1px solid #444}
.copyright{position:absolute;left:0;top:90px;width:717px;text-align:center;font-size:10px}
</style>
</head>
<body>
<div class="abs page"></div>

<div class="abs brand"><span class="brand-dot"></span><span class="brand-name">TQR</span></div>
<div class="abs social"><span>Vyn</span><span>Orb</span><span>Zel</span><span>Quo</span></div>

<nav class="abs nav">
  <a style="left:38px">Home</a><span class="sep" style="left:79px"></span>
  <a style="left:125px">Clients</a><span class="sep" style="left:168px"></span>
  <a style="left:255px">Basketball Bootcamp</a><span class="sep" style="left:343px"></span>
  <a style="left:427px">High School Services</a><span class="sep" style="left:513px"></span>
  <a style="left:552px">More...</a>
</nav>

<section class="abs hero">
  <div class="abs hero-player" role="img" aria-label="Photo of a basketball player in a red jersey holding a ball"></div>
  <div class="abs hero-net" role="img" aria-label="Photo of a red basketball dropping through a net"></div>
  <div class="abs hero-title">TQR</div>
  <div class="abs hero-sub">VANTAGE<br>CLINICS</div>
  <div class="abs hero-from">STARTING FROM</div>
  <div class="abs hero-date">10TH JUNE</div>
  <div class="abs hero-year">2013</div>
  <div class="abs signup">SIGN UP NOW!</div>
  <div class="abs dots"><i></i><i></i><i></i><i></i><i></i></div>
</section>

<div class="abs section-head red" style="left:196px;top:480px;width:353px">NEWS</div>
<div class="abs section-head red" style="left:560px;top:480px;width:353px">VIDEOS</div>

<div class="abs news-feature" role="img" aria-label="Photo of two players contesting the ball in a crowded arena"></div>
<div class="abs news-caption">Lorem ipsum dolor sit amet, consectetuer adipiscing elit,</div>

<article class="abs news-item" style="top:742px"><div class="thumb" role="img" aria-label="Game action photo"></div>
  <h3>Lobortis nisl ut aliquip ex eaexerci tation ullamcorper suscipit</h3><p class="meta">25 April, 2013 | 65 Comments</p></article>
<article class="abs news-item" style="top:814px"><div class="thumb" role="img" aria-label="Game action photo"></div>
  <h3>Lobortis nisl ut aliquip ex eaexerci tation ullamcorper suscipit</h3><p class="meta" style="top:38px">25 April, 2013 | 65 Comments</p></article>
<article class="abs news-item" style="top:886px"><div class="thumb" role="img" aria-label="Game action photo" style="background:linear-gradient(160deg,#1a2a6a,#3a6ab0 50%,#c9a22a)"></div>
  <h3>Lobortis nisl ut aliquip ex eaexerci tation ullamcorper suscipit</h3><p class="meta" style="top:38px">25 April, 2013 | 65 Comments</p></article>

<article class="abs video-item" style="top:532px">
  <div class="video-thumb" role="img" aria-label="Video still of a game"><svg width="118" height="81"><circle cx="59" cy="42" r="19" fill="#ddd" stroke="#999" stroke-width="2"/><path d="M54 35 L66 42 L54 49Z" fill="#111"/></svg></div>
  <h3>Exerci tation ullamcorper suscipit lobortis nisl ut aliquip ex ea</h3><p class="meta">65 Views</p></article>
<div class="abs video-rule" style="top:630px"></div>
<article class="abs video-item" style="top:642px">
  <div class="video-thumb" role="img" aria-label="Video still of a dunk from above"><svg width="118" height="81"><circle cx="59" cy="42" r="19" fill="#ddd" stroke="#999" stroke-width="2"/><path d="M54 35 L66 42 L54 49Z" fill="#111"/></svg></div>
  <h3>Lobortis nisl ut aliquip ex eaexerci tation ullamcorper suscipit</h3><p class="meta">59 Views</p></article>
<div class="abs video-rule" style="top:740px"></div>
<article class="abs video-item" style="top:751px">
  <div class="video-thumb" role="img" aria-label="Video still of a player at the rim" style="background:linear-gradient(150deg,#3a3a3a,#8a8a30 55%,#1a1a1a)"><svg width="118" height="81"><circle cx="59" cy="42" r="19" fill="#ddd" stroke="#999" stroke-width="2"/><path d="M54 35 L66 42 L54 49Z" fill="#111"/></svg></div>
  <h3>Nisl ut aliquip ex ea exerci tation ullamcorper suscipit lobortis</h3><p class="meta">37 Views</p></article>
<div class="abs video-rule" style="top:850px"></div>
<article class="abs video-item" style="top:860px">
  <div class="video-thumb" role="img" aria-label="Video still of a dunk from above"><svg width="118" height="81"><circle cx="59" cy="42" r="19" fill="#ddd" stroke="#999" stroke-width="2"/><path d="M54 35 L66 42 L54 49Z" fill="#111"/></svg></div>
  <h3>Tation ullamcorper<br>suscipit lobortis nisl ut aliquip ex ea Exerci</h3><p class="meta">57 Views</p></article>

<div class="abs section-head dark" style="left:196px;top:958px;width:717px">LINKS</div>

<div class="abs badges">
  <span class="badge" style="left:12px;width:28px"></span>
  <span class="badge" style="left:70px;width:32px"></span>
  <span class="badge" style="left:136px;width:36px;top:2px;height:48px"></span>
  <span class="badge" style="left:207px;width:22px;top:4px;height:46px"></span>
  <span class="badge" style="left:262px;width:42px"></span>
  <span class="badge" style="left:335px;width:100px;top:12px;height:26px"></span>
  <span class="badge" style="left:468px;width:64px;top:16px;height:18px"></span>
  <span class="badge" style="left:578px;width:28px;top:2px;height:48px"></span>
  <span class="badge" style="left:640px;width:64px;top:10px;height:30px;border-radius:15px"></span>
</div>

<footer class="abs footer">
  <div class="footer-mark"><i></i><b>TQR</b></div>
  <h4>Links</h4>
  <div class="footer-links"><span>Home</span><span>|</span><span>Clients</span><span>|</span><span>Basketball Bootcamp</span><span>|</span><span>High School Services</span><span>|</span><span>More...</span></div>
  <div class="footer-social"><span>Vyn</span><span>Orb</span><span>Zel</span><span>Quo</span></div>
  <div class="footer-rule"></div>
  <p class="copyright">Copyright 2013 TQR. All rights reserved.</p>
</footer>
</body>
</html>
```